buseisness card

design a card that similar to my web site
BRIXENTAPLORLLC .COM

Contact Information for Business Card

NAME PHONE # WEBSITE EMAIL AND DISCTIPTION OF WHAT WE DO

Colors
0054AA
0677BA
7BADD7
CADEEF
E8F1F8

Requirements
Must have
• lOGO AND DETAILS
Nice to have
• I LIKE THE WATER LIKE ON MY WEB SITE

```html
<!DOCTYPE html>
<html lang="en">
<head>
<meta charset="utf-8">
<title>Brixentaplor – Business Card Presentation</title>
<link href="https://fonts.googleapis.com/css2?family=Montserrat:wght@500;600&family=Open+Sans:ital,wght@0,400;0,600;0,700;1,400&display=swap" rel="stylesheet">
<style>
  :root{
    --deep:#0a2d78;
    --ocean:#0f4a95;
    --sea:#1a6fae;
    --teal:#2f8fb8;
    --sky:#7badd7;
    --ice:#c4e9f3;
    --card-navy:#0b2a7c;
    --rule:#5fa6e6;
    --ink:#0a237a;
    --white:#ffffff;
  }
  *{margin:0;padding:0;box-sizing:border-box}
  html,body{width:849px;height:1200px;overflow:hidden}
  body{font-family:"Open Sans",Arial,sans-serif;color:var(--white);position:relative}
  .backdrop{position:absolute;inset:0;
    background:radial-gradient(ellipse at 40% 12%,#3d8fc0 0%,transparent 45%),
      linear-gradient(180deg,#1a5a9a 0%,#1f77ad 16%,#1b6aa6 26%,#0e4c93 50%,#0a3a88 75%,#072f7c 100%)}
  .brand{position:absolute;left:0;width:849px;top:194px;text-align:center}
  .brand-name{font-family:"Montserrat",Arial,sans-serif;font-weight:500;font-size:26px;letter-spacing:.3px}
  .brand-tagline{font-family:"Montserrat",Arial,sans-serif;font-size:8.5px;font-weight:600;margin-top:2px}
  .card{position:absolute;top:322px;width:286px;height:515px;box-shadow:0 6px 14px rgba(0,10,50,.45);overflow:hidden}
  .card-front{left:120px;background:var(--card-navy)}
  .card-back{left:442px;background:var(--ice)}
  .water-band{position:absolute;left:0;width:100%;
    background:radial-gradient(ellipse at 55% 45%,#4f9bd0 0%,transparent 55%),linear-gradient(180deg,#0d3f95 0%,#1f6eb4 55%,#3a9cc6 100%)}
  .card-front .water-band{top:0;height:172px}
  .front-rule{position:absolute;top:172px;left:0;width:100%;height:3px;background:var(--rule)}
  .card-name{position:absolute;left:0;width:100%;text-align:center;font-family:"Montserrat",Arial,sans-serif;font-weight:500;font-size:17px}
  .card-front .card-name{top:120px}
  .person{position:absolute;left:46px;top:264px}
  .person-name{font-size:18px;font-weight:700}
  .person-role{font-size:14px;font-style:italic;color:var(--sky);margin-top:1px}
  .contacts{position:absolute;left:46px;top:372px;list-style:none;font-size:12.5px}
  .contacts li{display:flex;align-items:flex-start;margin-bottom:7px;line-height:17px}
  .contacts svg{width:12px;height:12px;margin:2px 10px 0 0;flex:none;fill:var(--sky)}
  .contacts .link{color:var(--sky)}
  .services{position:absolute;left:50px;right:50px;top:42px;color:var(--ink)}
  .services-lead{font-weight:700;font-size:12.5px;line-height:16px;text-align:justify}
  .services-list{list-style:none;margin-top:38px;font-size:12.5px;line-height:21px}
  .services-list li{display:flex;justify-content:space-between}
  .services-list b{font-weight:700}
  .slogan{position:absolute;left:0;width:100%;top:232px;text-align:center;color:var(--ink);font-weight:700;font-size:16px;line-height:22px}
  .back-rule{position:absolute;top:342px;left:0;width:100%;height:3px;background:var(--deep)}
  .card-back .water-band{top:345px;height:170px;
    background:radial-gradient(ellipse at 45% 75%,#4a96cc 0%,transparent 50%),linear-gradient(180deg,#3d9cc2 0%,#1e6fb0 40%,#0c3b91 100%)}
  .card-back .card-name{top:368px}
  .specs{position:absolute;left:100px;top:933px;width:650px;height:107px;border:2px solid var(--white);border-collapse:collapse;font-size:14px;letter-spacing:.6px}
  .specs table{width:100%;border-collapse:collapse;margin-top:5px}
  .specs td{height:32px;padding-left:26px;border-bottom:1px solid rgba(255,255,255,.6)}
  .specs tr:last-child td{border-bottom:none}
  .specs td.label{width:173px}
  .specs td.value{width:180px;border-left:1px solid rgba(255,255,255,.8);padding-left:24px}
  .specs td.label2{width:152px;padding-left:4px}
  .specs td.date{border-left:1px solid rgba(255,255,255,.8);padding-left:19px}
  .credit{position:absolute;right:103px;top:1063px;font-size:12px}
  .credit b{font-weight:700}
  .page-num{position:absolute;right:103px;top:1122px;font-size:12px}
</style>
</head>
<body>
  <div class="backdrop" role="img" aria-label="Underwater photograph of a sunlit ocean surface with bubbles"></div>

  <header class="brand">
    <div class="brand-name">BRIXENTAPLOR</div>
    <div class="brand-tagline">An Eco Friendly Company Doing Eco Friendly Testing</div>
  </header>

  <section class="card card-front">
    <div class="water-band" role="img" aria-label="Photograph of water surface with light bubbles"></div>
    <div class="card-name">BRIXENTAPLOR</div>
    <div class="front-rule"></div>
    <div class="person">
      <div class="person-name">Mr Daniel Varrow</div>
      <div class="person-role">founder</div>
    </div>
    <ul class="contacts">
      <li><svg viewBox="0 0 12 12"><path d="M6 0a4.2 4.2 0 0 0-4.2 4.2C1.8 7.4 6 12 6 12s4.2-4.6 4.2-7.8A4.2 4.2 0 0 0 6 0zm0 5.9a1.7 1.7 0 1 1 0-3.4 1.7 1.7 0 0 1 0 3.4z"/></svg><span>4180 Harborline Avenue<br>Dayton, OH 45402</span></li>
      <li><svg viewBox="0 0 12 12"><path d="M1 3h10v6.5H1z M1 3l5 3.6L11 3" fill="none" stroke="#7badd7" stroke-width="1.3"/><path d="M1 3h10L6 6.4z"/></svg><span class="link">dv@bx204.com</span></li>
      <li><svg viewBox="0 0 12 12"><path d="M2.4 0.8l2 2.2-1 1.4c.7 1.6 2 2.9 3.6 3.6l1.4-1 2.2 2-1.2 1.8C5.8 10.6 1.4 6.2 .6 2z"/></svg><span>(555) 318 4702</span></li>
      <li><svg viewBox="0 0 12 12"><circle cx="6" cy="6" r="5.2" fill="none" stroke="#7badd7" stroke-width="1.2"/><path d="M.8 6h10.4M6 .8c-2.4 3-2.4 7.4 0 10.4M6 .8c2.4 3 2.4 7.4 0 10.4" fill="none" stroke="#7badd7" stroke-width="1"/></svg><span class="link">www.brixentaplorllc.com</span></li>
    </ul>
  </section>

  <section class="card card-back">
    <div class="services">
      <p class="services-lead">Our 3 main types of foam with water testing services i.e :</p>
      <ul class="services-list">
        <li><span>High Expansion Foam</span><b>(HEF)</b></li>
        <li><span>Alcohol Resistant Foam</span><b>(AR)</b></li>
        <li><span>Aqueous Film Forming</span><b>(AFFF)</b></li>
      </ul>
    </div>
    <p class="slogan">Saving Time,<br>Money and the<br>Environment!</p>
    <div class="back-rule"></div>
    <div class="water-band" role="img" aria-label="Photograph of ocean surface with sparkling bubbles"></div>
    <div class="card-name">BRIXENTAPLOR</div>
  </section>

  <div class="specs">
    <table>
      <tr><td class="label">company :</td><td class="value">brixentaplor</td><td class="label2">dateline :</td><td class="date">05.10.2021</td></tr>
      <tr><td class="label">project title :</td><td class="value">business card</td><td class="label2">submission :</td><td class="date">03.10.2021</td></tr>
      <tr><td class="label">card size :</td><td class="value">5.0 x 9.0cm</td><td class="label2"></td><td class="date"></td></tr>
    </table>
  </div>

  <p class="credit">Stockwave : <b>Lena Marsh</b></p>
  <p class="page-num">pg. <b>1/1</b></p>
</body>
</html>
```